small auto electrical company needs new logo and business cards !!!

we are a small auto electrical company (Velmor Autos Ltd) that has been running for 13 years the logo we have was put together by dinosaurs so we are looking at re branding the company starting with business cards and a new logo we fit GPS tracking devices for young drivers through there insurance company also we fit hands free systems and dash cameras also safety locks to fleet vehicles we would like bright eye catching colours day glow and neon and quirky designs for the logo our original logo was baby blue which i have added a picture enclosed we would like double sided but have a space to write notes and prices preferably not white on back same colour throughout many thanks
Reason: Just a chance to finalise any designs we want VA logos or V logos - No vlm's and no dinosaurs lol
Business
Installs@velmorautos.co.uk
07922483617
www.Velmorautos.co.uk
Velmor Autos Ltd - Fleets and Insurance Services
- new logo design !!
- Satellite in logo or something attaining to gps
- maybe a car in the logo
- shouldnt have velmor as vlm it is VeLMOR Autos

```html
<!DOCTYPE html>
<html lang="en">
<head>
<meta charset="utf-8">
<title>Velmor Autos Ltd – Business Card</title>
<link href="https://fonts.googleapis.com/css2?family=Open+Sans:wght@400;700;800&display=swap" rel="stylesheet">
<style>
  :root {
    --canvas-bg: #e8e5e0;
    --card-dark: #0b0b0b;
    --card-dark-top: #1d1d1d;
    --card-light: #ffffff;
    --card-light-edge: #e2e2e2;
    --lime: #b5d334;
    --ink: #111111;
    --ink-soft: #2b2b2b;
    --silver: #e4e4e4;
  }
  * { box-sizing: border-box; margin: 0; padding: 0; }
  html, body { width: 1200px; height: 1200px; overflow: hidden; }
  body {
    background: var(--canvas-bg);
    font-family: "Open Sans", Arial, sans-serif;
    position: relative;
  }
  .card {
    position: absolute;
    left: 220px;
    width: 760px;
    height: 434px;
    border-radius: 26px;
    box-shadow: 0 18px 40px rgba(0,0,0,0.22);
  }
  .card--front {
    top: 120px;
    background: linear-gradient(180deg, var(--card-dark-top) 0%, var(--card-dark) 45%);
    display: flex;
    flex-direction: column;
    align-items: center;
    justify-content: center;
    gap: 34px;
  }
  .card--back {
    top: 640px;
    background: radial-gradient(ellipse at 55% 30%, var(--card-light) 55%, var(--card-light-edge) 100%);
  }
  .brand-dot {
    border-radius: 50%;
    background: var(--lime);
  }
  .card--front .brand-dot { width: 150px; height: 150px; }
  .brand-name {
    font-weight: 800;
    letter-spacing: 0.5px;
    white-space: nowrap;
  }
  .card--front .brand-name { color: var(--silver); font-size: 54px; }

  .back-brand {
    position: absolute;
    left: 70px;
    top: 110px;
    width: 300px;
    display: flex;
    flex-direction: column;
    align-items: center;
    gap: 22px;
  }
  .back-brand .brand-dot { width: 112px; height: 112px; }
  .back-brand .brand-name { color: var(--ink); font-size: 32px; }

  .contact {
    position: absolute;
    left: 470px;
    top: 165px;
    color: var(--ink-soft);
  }
  .contact__name {
    font-size: 32px;
    font-weight: 400;
    margin-bottom: 22px;
    white-space: nowrap;
  }
  .contact__name strong { font-weight: 700; }
  .contact__row {
    display: flex;
    align-items: center;
    gap: 16px;
    font-size: 20px;
    margin-bottom: 14px;
    white-space: nowrap;
  }
  .contact__icon { width: 22px; height: 18px; flex: none; }
</style>
</head>
<body>
  <section class="card card--front" aria-label="Card front">
    <div class="brand-dot" aria-hidden="true"></div>
    <p class="brand-name">Velmor Autos Ltd</p>
  </section>

  <section class="card card--back" aria-label="Card back">
    <div class="back-brand">
      <div class="brand-dot" aria-hidden="true"></div>
      <p class="brand-name">Velmor Autos Ltd</p>
    </div>

    <div class="contact">
      <p class="contact__name">Your <strong>Name</strong></p>
      <p class="contact__row">
        <svg class="contact__icon" viewBox="0 0 22 18" aria-hidden="true">
          <path d="M1 6 Q11 -1 21 6 L18 8 L15 6 L15 4 Q11 3 7 4 L7 6 L4 8 Z" fill="var(--lime)"/>
          <path d="M5 9 L17 9 L20 17 L2 17 Z" fill="var(--lime)"/>
          <circle cx="11" cy="13" r="2.4" fill="#fff"/>
        </svg>
        000 000 0000
      </p>
      <p class="contact__row">
        <svg class="contact__icon" viewBox="0 0 22 18" aria-hidden="true">
          <rect x="1" y="2" width="20" height="14" fill="var(--lime)"/>
          <path d="M1 2 L11 10 L21 2" fill="none" stroke="#fff" stroke-width="1.6"/>
        </svg>
        youremail@xyz.com
      </p>
    </div>
  </section>
</body>
</html>
```